Course flyer - evolutive design

We want to have a nice design for our course programm.
In fact we are school language, and our course programm change approximatively each 2 weeks§.
For that we need a design that we can modify each 2 weeks (only dates change ) by ourselves.
We used to have a classical design but we want to upgrade it with a modern and attractive design.
We can have 3 versions one for each city.
We have 3 offices: Tunis, Sousse & Sfax
Attached you can find old designs

Target Market(s)

students from 16 years old till retired people 76 years old

Industry/Entity Type

Education

Font styles to use
Sans Serif

Requirements
Must have
• clear timing for courses (date, days, timing)
• prices
• Adresse (each flyer has its own adress)
• phone Number
• Cool image
Should not have
• Racism
• Violence
• Too much stuff

```html
<!DOCTYPE html>
<html lang="fr">
<head>
<meta charset="utf-8">
<title>Cours d'allemand – Sfax</title>
<link href="https://fonts.googleapis.com/css2?family=Fjalla+One&family=Open+Sans:wght@400;600;700&family=Open+Sans+Condensed:wght@700&display=swap" rel="stylesheet">
<style>
  :root{
    --teal:#1f7f78;
    --lime:#cfdc2e;
    --ink:#1b1b1b;
    --footer-dark:#1c1c1c;
    --panel:rgba(255,255,255,.86);
    --text:#2a2a2a;
  }
  *{margin:0;padding:0;box-sizing:border-box}
  html,body{width:848px;height:1200px;overflow:hidden}
  body{position:relative;font-family:"Open Sans",Arial,sans-serif;color:var(--text);background:#eee}

  .backdrop{position:absolute;left:0;top:0;width:848px;height:1013px;
    background:
      linear-gradient(180deg,rgba(240,236,238,0) 55%,rgba(120,110,120,.35) 100%),
      linear-gradient(90deg,#e9dfe4 0%,#f2f1f2 45%,#e6e9e9 100%);}
  .group-photo{position:absolute;left:0;top:650px;width:848px;height:363px;
    background:linear-gradient(90deg,#c9546a 0%,#8a8fa6 30%,#3f9a8c 48%,#9aa1b5 70%,#4a4f72 100%);
    opacity:.55}

  .title{position:absolute;left:30px;top:28px;font-family:"Fjalla One",sans-serif;
    font-size:86px;line-height:1;color:var(--ink);letter-spacing:.5px}
  .period{position:absolute;left:693px;top:38px;width:135px;height:80px;background:var(--lime);
    display:flex;align-items:center;justify-content:center;gap:6px}
  .period .year{font-family:"Fjalla One",sans-serif;color:var(--teal);font-size:24px;
    writing-mode:vertical-rl;transform:rotate(180deg);line-height:1}
  .period .months{font-family:"Fjalla One",sans-serif;color:var(--ink);font-size:30px;line-height:1}

  .brand{position:absolute;left:55px;top:330px;font-family:"Fjalla One",sans-serif;
    font-size:118px;line-height:1;color:var(--ink);letter-spacing:-2px}

  .course{position:absolute;left:452px;width:376px}
  .course-name{background:var(--teal);color:var(--lime);font-family:"Fjalla One",sans-serif;
    font-size:38px;height:58px;line-height:58px;padding-left:20px}
  .course-body{background:var(--panel);padding:10px 20px 12px}
  .course-dates{font-family:"Open Sans Condensed",sans-serif;font-weight:700;color:var(--teal);font-size:20px;text-transform:uppercase}
  .course-days{font-size:19px;margin-top:4px}
  .course-hours{font-size:20px;font-weight:700;margin-top:4px}
  .course-price{font-size:18px;margin-top:4px}
  .course-note{font-size:12px;margin-top:10px}
  .super{top:193px}
  .intensif{top:398px}
  .extensif{top:603px}

  .footer{position:absolute;left:0;top:1013px;width:848px;height:187px;display:flex}
  .office{width:222px;background:var(--teal);color:#fff;padding:18px 0 0 20px}
  .office-city{font-family:"Fjalla One",sans-serif;font-size:28px;line-height:1.1}
  .office-address{font-size:16px;line-height:1.55;margin-top:6px}
  .contact{flex:1;background:var(--footer-dark);color:#fff;display:flex;padding:20px 20px 0 22px}
  .contact-lines{width:372px;font-family:"Open Sans Condensed",sans-serif;font-weight:700;font-size:16px;line-height:1.55;text-transform:uppercase}
  .phone{display:flex;align-items:baseline;gap:8px}
  .phone b{font-size:20px}
  .phone span{color:var(--lime);font-family:"Fjalla One",sans-serif;font-size:36px;line-height:1}
  .terms{flex:1;font-size:12.5px;line-height:1.35;padding-left:16px}
</style>
</head>
<body>
  <div class="backdrop" role="img" aria-label="Photo d'un mur de briques blanches en arrière-plan"></div>
  <div class="group-photo" role="img" aria-label="Photo de jeunes étudiants souriants assis ensemble, regardant leurs téléphones"></div>

  <h1 class="title">COURS D’ALLEMAND</h1>
  <div class="period"><span class="year">2016</span><span class="months">MAI<br>JUIN</span></div>

  <div class="brand">lernova</div>

  <section class="course super">
    <h2 class="course-name">SUPER INTENSIF</h2>
    <div class="course-body">
      <p class="course-dates">Du 13 au 24 juin 2016</p>
      <p class="course-days">Du Lundi au Vendredi</p>
      <p class="course-hours">9:00 À 13:30 &amp; 13:30 À 18:00</p>
      <p class="course-price">390 dt.</p>
    </div>
  </section>

  <section class="course intensif">
    <h2 class="course-name">INTENSIF</h2>
    <div class="course-body">
      <p class="course-dates">Du 20 juin au 15 juillet 2016*</p>
      <p class="course-days">Du Lundi au Vendredi</p>
      <p class="course-hours">9:00 À 13:30 &amp; 13:30 À 18:00</p>
      <p class="course-price">350 dt.</p>
    </div>
  </section>

  <section class="course extensif">
    <h2 class="course-name">EXTENSIF</h2>
    <div class="course-body">
      <p class="course-dates">Du 30 mai au 13 juillet *</p>
      <p class="course-days">Du Lundi au Vendredi</p>
      <p class="course-hours">9:00 À 13:30 &amp; 13:30 À 18:00</p>
      <p class="course-price">340 dt.</p>
      <p class="course-note">* prolongé par 3 jours à cause d'eid al fitr</p>
    </div>
  </section>

  <footer class="footer">
    <div class="office">
      <p class="office-city">SFAX</p>
      <p class="office-address">Avenue des Oliviers<br>Rue Ibn Khaldoun<br>Immeuble Yasmine<br>(5ème étage)</p>
    </div>
    <div class="contact">
      <div class="contact-lines">
        <p class="phone"><b>Tél:</b><span>71 234 560</span></p>
        <p>Email: sfax@lernova.org</p>
        <p>www.lernova.org</p>
        <p>Imm. Yasmine, 5ème étage Rue Ibn Khaldoun<br>(en face de la poste) 3000 Sfax</p>
      </div>
      <p class="terms">Toute inscription doit impérativement se faire au plus tard une semaine avant le début des cours. Nombre minimum de 4 participants requis. L'horaire des cours est susceptible d'être modifié. Prix par module 340 TND.</p>
    </div>
  </footer>
</body>
</html>
```